Calloway Holdings Website Design

We are a private equity firm based with offices based in Hong Kong, Singapore, London and Paris. Our focus is investments in property development projects, corporate ventures and loans.

We require the development of a new website and you will have to select relevant images from the likes of PixelVaultPics or other stock photo libraries.

We will need a design done for a PC based website and the designer selected with the favored design will also need to produce some concepts for a responsive website.

Target Market(s)

Sophisticated investors looking to invest in high return property development, businesses and mortgages.

Industry/Entity Type

Investment

Number of Pages Required

5+ page

Font styles to use
Serif
Sans Serif

Colors
0255a3
00a990

Requirements
Must have
• Clean modern feel and must portray stability and professionalism.

```html
<!DOCTYPE html>
<html lang="en">
<head>
<meta charset="utf-8">
<title>Calloway Holdings</title>
<link rel="stylesheet" href="https://fonts.googleapis.com/css2?family=Raleway:wght@400;500;600;700&family=Open+Sans:wght@400;600;700&display=swap">
<style>
:root{
  --blue:#0255a3;
  --green:#00a990;
  --sky:#3fb3d8;
  --ink:#222;
  --text:#444;
  --grey:#e4e4e4;
  --white:#fff;
}
*{margin:0;padding:0;box-sizing:border-box}
html,body{width:1200px;height:2970px;overflow:hidden}
body{font-family:"Open Sans",sans-serif;color:var(--text);background:var(--white);position:relative}

/* header */
.site-header{position:absolute;top:0;left:0;width:1200px;height:158px}
.phone{position:absolute;left:60px;top:48px;font-family:"Raleway",sans-serif;font-size:22px;color:var(--ink);letter-spacing:.5px}
.top-tools{position:absolute;right:50px;top:12px;display:flex;align-items:center;gap:6px}
.diamond{width:18px;height:18px;background:#111;transform:rotate(45deg);margin:0 5px}
.lang{font-size:11px;color:#333;margin-left:22px;display:flex;align-items:center;gap:5px}
.lang-box{width:14px;height:10px;background:var(--blue)}
.main-nav{position:absolute;top:115px;left:0;width:1200px;height:43px;background:var(--blue)}
.main-nav a{position:absolute;top:11px;color:var(--white);text-decoration:none;font-family:"Raleway",sans-serif;font-size:16px;font-weight:500}
.search-icon{position:absolute;right:48px;top:10px}
.logo-tab{position:absolute;left:520px;top:0;width:160px;height:158px;background:var(--white);border-radius:0 0 80px 80px;display:flex;flex-direction:column;align-items:center;justify-content:center;gap:6px;padding-top:10px}
.logo-mark{width:34px;height:34px;border-radius:50%;background:var(--blue)}
.logo-name{font-family:"Raleway",sans-serif;font-weight:700;font-size:15px;color:var(--blue);text-align:center;line-height:1.15;letter-spacing:1px}

/* hero */
.hero{position:absolute;top:158px;left:0;width:1200px;height:492px;background:linear-gradient(180deg,#eef1f4 0%,#c9d0d8 45%,#a9b3bd 75%,#d8dde2 100%)}
.hero-copy{position:absolute;left:86px;top:92px;width:560px}
.hero-title{font-family:"Raleway",sans-serif;font-size:34px;font-weight:700;color:var(--blue);line-height:1.35;letter-spacing:.5px}
.hero-title span{display:block;color:var(--green);font-weight:500}
.hero-text{font-family:"Raleway",sans-serif;font-size:21px;color:#333;line-height:1.35;margin-top:8px;width:470px}
.btn-subscribe{display:inline-block;margin-top:22px;margin-left:6px;background:var(--green);color:var(--white);font-family:"Raleway",sans-serif;font-size:21px;font-weight:600;padding:12px 22px;border-radius:6px}

/* who are you */
.who{position:absolute;top:650px;left:0;width:1200px;height:752px;text-align:center}
.section-title{font-family:"Raleway",sans-serif;font-size:34px;font-weight:600;letter-spacing:.5px}
.who .section-title{color:var(--blue);margin-top:28px}
.who-intro{font-size:15px;color:#444;margin-top:14px}
.roles{position:absolute;top:146px;left:80px;width:1040px;height:580px}
.role{position:absolute;top:0;width:244px;height:532px}
.role-panel{position:absolute;inset:0;background:var(--grey);clip-path:polygon(50% 0,100% 60px,100% 100%,0 100%,0 60px)}
.hex{position:absolute;left:28px;top:30px;width:190px;height:214px;clip-path:polygon(50% 0,100% 25%,100% 75%,50% 100%,0 75%,0 25%);background:#7a7a7a}
.hex-photo{position:absolute;inset:4px;clip-path:polygon(50% 0,100% 25%,100% 75%,50% 100%,0 75%,0 25%)}
.role-name{position:absolute;left:0;width:244px;top:268px;font-family:"Raleway",sans-serif;font-size:21px;color:var(--ink);line-height:1.45;letter-spacing:.5px}
.role-desc{position:absolute;left:16px;width:212px;font-size:13px;line-height:1.55;color:#444;text-align:justify;text-align-last:center;hyphens:auto;-webkit-hyphens:auto}
.role.active .role-name{color:var(--blue);font-size:29px;top:262px}
.view-details{position:absolute;left:0;bottom:0;width:244px;height:52px;background:var(--green);color:var(--white);font-family:"Raleway",sans-serif;font-size:16px;line-height:52px}

/* process */
.process{position:absolute;top:1402px;left:0;width:1200px;height:513px;background:var(--blue);color:var(--white);text-align:center}
.process .section-title{color:var(--white);margin-top:26px}
.step{position:absolute;top:126px;width:390px}
.step-icon{width:106px;height:106px;border-radius:50%;background:var(--white);margin:0 auto;display:flex;align-items:center;justify-content:center}
.step-title{font-family:"Raleway",sans-serif;font-size:26px;font-weight:600;margin-top:30px;letter-spacing:.5px}
.step-text{font-size:13px;line-height:1.8;margin:10px auto 0;width:340px}
.read-more{font-size:13px;font-weight:700;margin-top:12px;display:block}
.step-arrow{position:absolute;top:178px;width:190px;height:12px}

/* news */
.news{position:absolute;top:1915px;left:0;width:1200px;height:330px}
.news .section-title{color:var(--ink);font-weight:500;text-align:center;margin-top:42px}
.news-item{position:absolute;top:122px;width:370px;display:flex;gap:14px}
.news-date{font-family:"Raleway",sans-serif;font-size:50px;font-weight:600;color:var(--sky);line-height:.98;flex:0 0 auto}
.news-body{flex:1 1 auto;min-width:0}
.news-head{font-size:13.5px;font-weight:600;color:var(--ink);white-space:nowrap}
.news-text{font-size:13px;line-height:1.8;color:#444;margin-top:6px;text-align:justify}

/* experts */
.experts{position:absolute;top:2245px;left:0;width:1200px;height:422px;background:linear-gradient(90deg,#1d1d1f 0%,#333 45%,#2c2d30 70%,#1a1a1c 100%);text-align:center;color:var(--white)}
.experts .section-title{color:var(--white);font-weight:500;margin-top:42px}
.quote{font-size:15.5px;line-height:1.7;width:1040px;margin:20px auto 0;text-align:center}
.quote-author{color:var(--green);font-size:15px;margin-top:22px}
.dots{display:flex;justify-content:center;gap:8px;margin-top:20px}
.dots span{width:34px;height:5px;background:#ddd}
.dots span:first-child{background:var(--blue)}
.btn-outline{display:inline-block;margin-top:32px;border:2px solid var(--white);padding:11px 38px;font-size:13px;font-weight:600}

/* footer */
.site-footer{position:absolute;top:2667px;left:0;width:1200px;height:303px;background:var(--blue);color:var(--white);text-align:center}
.footer-logo{display:flex;flex-direction:column;align-items:center;gap:8px;margin-top:30px}
.footer-logo .logo-mark{background:var(--white);width:40px;height:40px}
.footer-logo .logo-name{color:var(--white);font-size:16px}
.footer-links{font-family:"Raleway",sans-serif;font-size:16px;margin-top:24px;letter-spacing:.5px}
.copyright{font-size:15px;margin-top:12px}
.footer-social{display:flex;justify-content:center;gap:18px;margin-top:40px}
.footer-social .diamond{width:26px;height:26px}
</style>
</head>
<body>

<header class="site-header">
  <div class="phone">+44 20 5550 0172</div>
  <div class="top-tools">
    <span class="diamond"></span><span class="diamond"></span><span class="diamond"></span><span class="diamond"></span>
    <span class="lang"><span class="lang-box"></span>English ▾</span>
  </div>
  <nav class="main-nav">
    <a style="left:78px">Home</a>
    <a style="left:184px">Services</a>
    <a style="left:308px">Investment Approach</a>
    <a style="left:733px">Missions and Values</a>
    <a style="left:944px">Contact</a>
    <svg class="search-icon" width="24" height="24" viewBox="0 0 24 24"><circle cx="9" cy="9" r="6.5" fill="none" stroke="#fff" stroke-width="2.5"/><line x1="14" y1="14" x2="22" y2="22" stroke="#fff" stroke-width="3"/></svg>
  </nav>
  <div class="logo-tab">
    <span class="logo-mark"></span>
    <div class="logo-name">CALLOWAY<br>HOLDINGS</div>
  </div>
</header>

<section class="hero" role="img" aria-label="Businessman in a suit standing on a balcony overlooking a city skyline">
  <div class="hero-copy">
    <h1 class="hero-title">HOW BEST TO REACH YOUR<span>TARGET AUDIENCE ?</span></h1>
    <p class="hero-text">THE NORTHGATE REVIEW OF DIGITAL MARKETING – contains the latest insights of top practitioners.</p>
    <span class="btn-subscribe">Subscribe today</span>
  </div>
</section>

<section class="who">
  <h2 class="section-title">WHO ARE YOU?</h2>
  <p class="who-intro">If you're part of a financial organisation, we have the power to help everyone work more efficiently, productively and profitably.</p>
  <div class="roles">
    <div class="role" style="left:0">
      <div class="hex"><div class="hex-photo" role="img" aria-label="Portrait of a senior executive in a suit" style="background:linear-gradient(160deg,#d9dde2,#5c6570)"></div></div>
      <div class="role-name" style="font-size:19px">Senior Hedge Fund<br>Manager/CEO</div>
      <p class="role-desc" style="top:342px">You need to develop and implement strategies for business growth, while ensuring profitability. You're aware your biggest asset is your staff and a happy workforce is a productive one.</p>
    </div>
    <div class="role active" style="left:270px">
      <div class="role-panel"></div>
      <div class="hex" style="top:40px"><div class="hex-photo" role="img" aria-label="Hands signing a document at a desk" style="background:linear-gradient(160deg,#b9c3cc,#eef0f2 55%,#8c96a0)"></div></div>
      <div class="role-name">CFO</div>
      <p class="role-desc" style="top:310px">You need to develop and implement strategies for business growth, while ensuring profitability. You're aware your biggest asset is your staff and a happy workforce is a productive one.</p>
      <div class="view-details">View details →</div>
    </div>
    <div class="role" style="left:530px">
      <div class="hex"><div class="hex-photo" role="img" aria-label="Group of business people at a press conference" style="background:linear-gradient(160deg,#6f757c,#2f3438)"></div></div>
      <div class="role-name" style="top:282px">IT Manager/CTO</div>
      <p class="role-desc" style="top:342px">You need to develop and implement strategies for business growth, while ensuring profitability. You're aware your biggest asset is your staff and a happy workforce is a productive one.</p>
    </div>
    <div class="role" style="left:800px">
      <div class="hex"><div class="hex-photo" role="img" aria-label="Two employees working together at an office desk" style="background:linear-gradient(160deg,#e9ecef,#9aa6b3)"></div></div>
      <div class="role-name" style="top:282px">Employee</div>
      <p class="role-desc" style="top:342px">You need to develop and implement strategies for business growth, while ensuring profitability. You're aware your biggest asset is your staff and a happy workforce is a productive one.</p>
    </div>
  </div>
</section>

<section class="process">
  <h2 class="section-title">OUR PROCESS</h2>
  <div class="step" style="left:28px">
    <div class="step-icon">
      <svg width="110" height="110" viewBox="0 0 110 110"><path d="M55 55 L55 27 A28 28 0 1 0 83 55 Z" fill="#0255a3"/><path d="M59 51 L59 23 A28 28 0 0 1 87 51 Z" fill="#0255a3"/><line x1="55" y1="27" x2="55" y2="83" stroke="#fff" stroke-width="3"/><line x1="27" y1="55" x2="83" y2="55" stroke="#fff" stroke-width="3"/></svg>
    </div>
    <h3 class="step-title">ANALYSIS &amp; ASSESSMENT</h3>
    <p class="step-text">Viewing key business metrics in an intuitive format enables empowered management to quickly make critical operating decisions; intelligent sales force deployment, re-alignment of marketing initiatives, risk concentration analysis for the insurance industry, or human capital optimization.</p>
    <span class="read-more">READ MORE</span>
  </div>
  <svg class="step-arrow" style="left:315px" viewBox="0 0 190 12"><line x1="0" y1="6" x2="190" y2="6" stroke="#fff" stroke-width="1.5"/><path d="M88 2 L94 6 L88 10" fill="none" stroke="#fff" stroke-width="1.5"/></svg>
  <div class="step" style="left:403px">
    <div class="step-icon">
      <svg width="70" height="70" viewBox="0 0 70 70"><path d="M12 38 L28 54 L60 18" fill="none" stroke="#0255a3" stroke-width="8" stroke-linecap="round" stroke-linejoin="round"/></svg>
    </div>
    <h3 class="step-title">IMPLEMENTATION</h3>
    <p class="step-text">Viewing key business metrics in an intuitive format enables empowered management to quickly make critical operating decisions; intelligent sales force deployment, re-alignment of marketing initiatives, risk concentration analysis for the insurance industry, or human capital optimization.</p>
    <span class="read-more">READ MORE</span>
  </div>
  <svg class="step-arrow" style="left:690px" viewBox="0 0 190 12"><line x1="0" y1="6" x2="190" y2="6" stroke="#fff" stroke-width="1.5"/><path d="M88 2 L94 6 L88 10" fill="none" stroke="#fff" stroke-width="1.5"/></svg>
  <div class="step" style="left:790px">
    <div class="step-icon">
      <svg width="70" height="70" viewBox="0 0 70 70"><rect x="24" y="10" width="38" height="28" fill="none" stroke="#0255a3" stroke-width="4"/><line x1="43" y1="38" x2="43" y2="58" stroke="#0255a3" stroke-width="4"/><rect x="8" y="30" width="14" height="30" rx="3" fill="#0255a3"/></svg>
    </div>
    <h3 class="step-title">ADAPT AND GROW</h3>
    <p class="step-text">Viewing key business metrics in an intuitive format enables empowered management to quickly make critical operating decisions; intelligent sales force deployment, re-alignment of marketing initiatives, risk concentration analysis for the insurance industry, or human capital optimization.</p>
    <span class="read-more">READ MORE</span>
  </div>
</section>

<section class="news">
  <h2 class="section-title">Latest News</h2>
  <article class="news-item" style="left:50px">
    <div class="news-date">24/<br>08</div>
    <div class="news-body"><h3 class="news-head">Nexora signs Joint Venture with BRAVELIN</h3><p class="news-text">Nexora Software Inc. and BRAVELIN Solutions are pleased to announce a new joint venture aimed at providing our</p></div>
  </article>
  <article class="news-item" style="left:432px">
    <div class="news-date">20/<br>08</div>
    <div class="news-body"><h3 class="news-head">Nexora signs Joint Venture with BRAVELIN</h3><p class="news-text">Nexora Software Inc. and BRAVELIN Solutions are pleased to announce a new joint venture aimed at providing our</p></div>
  </article>
  <article class="news-item" style="left:812px">
    <div class="news-date">10/<br>08</div>
    <div class="news-body"><h3 class="news-head">Nexora signs Joint Venture with BRAVELIN</h3><p class="news-text">Nexora Software Inc. and BRAVELIN Solutions are pleased to announce a new joint venture aimed at providing our</p></div>
  </article>
</section>

<section class="experts" role="img" aria-label="Dark background photo of a businessman in a suit and red tie">
  <h2 class="section-title">Ask Our Experts</h2>
  <p class="quote">"Nexora Software's reputation for extensive knowledge of business intelligence analytics has a well-founded basis. Partnering with them was a win-win from day one onward, repeatedly demonstrated by our teams working together in unified fashion to quickly identify and resolve technical issues while delivering highly valued solutions that solved difficult market problems. A solid talented group of professionals who are a pleasure to engage with."</p>
  <p class="quote-author">Dr. Alan Verity, Vice President/General Manager - Analytics, Leading Healthcare IT Company</p>
  <div class="dots"><span></span><span></span><span></span></div>
  <span class="btn-outline">READ MORE</span>
</section>

<footer class="site-footer">
  <div class="footer-logo">
    <span class="logo-mark"></span>
    <div class="logo-name">CALLOWAY<br>HOLDINGS</div>
  </div>
  <p class="footer-links">HOME • SOLUTIONS • SERVICES • COMPANY • CONTACT</p>
  <p class="copyright">Copyright © 2007 - 2015 calloway holdings, Inc. All Rights Reserved</p>
  <div class="footer-social"><span class="diamond"></span><span class="diamond"></span><span class="diamond"></span><span class="diamond"></span></div>
</footer>

</body>
</html>
```